Residential Construction Business - Site Signage

I need a design made for a site fence banner. We have a logo and branding so the design would need to be aligned with this. It would need to be made to specific size ratio so that it can be sent to the maker for production.
ratio : 4600 wide x 1700 high
The design should feature our website and also the slogan
"don't move, re-imagine"

Target Market(s)

potential clients

Industry/Entity Type

construction

Font styles to use
Other font styles liked:
• to match branding

Colors
0054AA
0677BA
7BADD7
CADEEF
E8F1F8

Requirements
Must have
• www.velmarbuild.com.au Majority of the sign is our brand logo
Nice to have
• Majority of the sign is our brand logo
Should not have
• colors and themes that arent brand relevant

```html
<!DOCTYPE html>
<html lang="en">
<head>
<meta charset="utf-8">
<title>Velmar Build – Site Fence Banner</title>
<link href="https://fonts.googleapis.com/css2?family=Montserrat:wght@500;600&family=Poppins:wght@400;600;700&display=swap" rel="stylesheet">
<style>
  :root {
    --backdrop: #d4d4d4;
    --banner-white: #ffffff;
    --brand-navy: #053c5d;
    --brand-navy-deep: #12354f;
    --text-light: #ffffff;
  }
  html, body {
    margin: 0;
    padding: 0;
    width: 1200px;
    height: 840px;
    overflow: hidden;
    background: var(--backdrop);
  }
  .fence-banner {
    display: block;
    width: 1200px;
    height: 840px;
  }
  .banner-sheet { fill: var(--banner-white); }
  .brand-panel { fill: url(#panelTone); }
  .brand-name {
    font-family: "Montserrat", sans-serif;
    font-weight: 500;
    font-size: 32px;
    fill: var(--text-light);
  }
  .divider { stroke: var(--text-light); stroke-width: 1.5; }
  .slogan {
    font-family: "Poppins", sans-serif;
    font-weight: 700;
    font-size: 57px;
    fill: var(--text-light);
  }
  .tagline {
    font-family: "Poppins", sans-serif;
    font-weight: 400;
    font-size: 31px;
    fill: var(--text-light);
  }
  .web-address {
    font-family: "Poppins", sans-serif;
    font-weight: 400;
    font-size: 31px;
    fill: var(--text-light);
  }
  .web-address .domain { font-weight: 600; }
</style>
</head>
<body>
<svg class="fence-banner" viewBox="0 0 1200 840" xmlns="http://www.w3.org/2000/svg" role="img" aria-label="Velmar Build site fence banner: Don't move, re-imagine. Expert renovations for Brisbane living. www.velmarbuild.com.au">
  <defs>
    <linearGradient id="panelTone" x1="0" y1="0" x2="1" y2="0">
      <stop offset="0" stop-color="#053c5d"/>
      <stop offset="0.7" stop-color="#073d60"/>
      <stop offset="1" stop-color="#12354f"/>
    </linearGradient>
    <filter id="sheetShadow" x="-5%" y="-5%" width="110%" height="115%">
      <feDropShadow dx="0" dy="2" stdDeviation="2.5" flood-color="#000" flood-opacity="0.35"/>
    </filter>
  </defs>

  <rect class="banner-sheet" x="19" y="204" width="1161" height="431" filter="url(#sheetShadow)"/>

  <path class="brand-panel" d="M421 205 L1179 205 L1179 634 L422 634 L253 443 Q243 430 243 417 Q243 404 253 392 Z"
        role="img" aria-label="Brand panel with soft geometric background texture"/>

  <text class="brand-name" x="262" y="431" textLength="372" lengthAdjust="spacing">VELMAR BUILD</text>

  <line class="divider" x1="670.5" y1="305" x2="670.5" y2="496"/>

  <text class="slogan" x="708" y="346" textLength="423" lengthAdjust="spacingAndGlyphs">DON'T MOVE,</text>
  <text class="slogan" x="708" y="401" textLength="390" lengthAdjust="spacingAndGlyphs">RE-IMAGINE</text>

  <text class="tagline" x="709" y="453" textLength="367" lengthAdjust="spacingAndGlyphs">EXPERT RENOVATIONS</text>
  <text class="tagline" x="709" y="492" textLength="353" lengthAdjust="spacingAndGlyphs">FOR BRISBANE LIVING</text>

  <text class="web-address" x="628" y="598" textLength="502" lengthAdjust="spacingAndGlyphs">www.<tspan class="domain">velmarbuild</tspan>.com.au</text>
</svg>
</body>
</html>
```